Brisk Tails Dog Behaviour, Training and Natural Healthcare Website

Hey there,
I need a webpage designed for my new business. It needs to be something authentic, new, fresh and representative of my business ethos. I operate out of Newcastle, NSW. I believe my job is to keep dogs alive and in their home by promoting communication and connection between dogs and their owners. This can't be achieved through training and behaviour alone. Nutritional guidance and environmental adaptation are often needed to complete the package and increase the success rate for these programs. I provide practical services such as walking coaching, nutrition profiling, behavioural modification, puppy minding, board and train programs for puppies and young dogs, training, basic and complex skills training, physical therapies and natural healthcare options. In effect taking care of the whole dog.
My motto is = Happy dogs, happy owners.
My catch cry is = promoting communication and connection between dogs and their owners.

I have in mind pages that can also link to other pages when an icon is clicked. I need a homepage, sections to explain what each of my services do (4 - which could be independent pages so I can attach photos) and a gallery. I want to have multi page function, an online capability for future retail, ability to amend and update content myself, an online booking and payment facility. My interests lie in I have seen many successes via and environmental modifications.
I've attached the logo which features prominently on my business card and Facebook page. The corporate colours are Blue with a splash of red and white. The dog being held in the healing hands must feature.

Thanks!

Australian Pet Dog Owners

Communication

Colors
0355a3
ec1f27
ffffff

Requirements
Must have
• The business colours (blue with a splash of red and white), the dog in the healing hands
Should not have
• Pawprints or cartoon animals

```html
<!DOCTYPE html>
<html lang="en">
<head>
<meta charset="utf-8">
<title>Brisk Tails — Happy Dogs, Happy Owners</title>
<link rel="stylesheet" href="https://fonts.googleapis.com/css2?family=Raleway:wght@400;500;600&family=Open+Sans:wght@400;600&display=swap">
<style>
:root{
  --sky-top:#0b8fd9;
  --sky-bottom:#0a5cb5;
  --navy:#0d3f97;
  --navy-deep:#0a2f78;
  --red:#e31b23;
  --red-dark:#b5101a;
  --white:#ffffff;
  --ink:#3b3b3b;
  --line:#d9d9d9;
  --footer:#efefef;
  --blue-text:#0d4fa0;
  --amber:#f5b31a;
  --amber-text:#e9a41a;
  --green:#6cbd1f;
  --green-text:#5fa51a;
  --grey-icon:#7b7b7b;
}
*{margin:0;padding:0;box-sizing:border-box}
html,body{width:1168px;height:1200px;overflow:hidden}
body{
  position:relative;
  font-family:"Open Sans",Arial,sans-serif;
  color:var(--ink);
  background:linear-gradient(180deg,var(--sky-top) 0%,#0b7bcc 45%,var(--sky-bottom) 100%);
}
.abs{position:absolute}

/* brand tab */
.brand{left:130px;top:0;width:217px;height:167px;
  background:linear-gradient(180deg,#1b5fbf 0%,var(--navy) 60%,var(--navy-deep) 100%);
  border-radius:0 0 10px 10px;box-shadow:0 4px 10px rgba(0,0,0,.3);
  text-align:center;color:var(--white);font-family:"Raleway",sans-serif;z-index:3}
.brand-mark{position:absolute;left:67px;top:14px;width:82px;height:82px;border-radius:50%;
  background:#f1e2b8;border:5px solid #c7222a}
.brand-name{position:absolute;left:0;right:0;top:103px;font-size:23px;font-weight:500;letter-spacing:.5px}
.brand-tag{position:absolute;left:0;right:0;top:132px;font-size:11px;font-weight:500}

/* contact */
.call{right:132px;top:36px;text-align:right;font-family:"Raleway",sans-serif}
.call-label{font-size:14px;color:var(--navy);font-weight:500}
.call-number{font-size:17px;color:var(--white);display:flex;align-items:center;gap:4px;justify-content:flex-end}

/* nav */
.nav{left:347px;top:87px;width:688px;height:41px;background:var(--red);display:flex;
  font-family:"Raleway",sans-serif;font-size:14.5px;color:var(--white)}
.nav span{display:flex;align-items:center;justify-content:center;border-right:1px solid rgba(0,0,0,.15);flex:auto}
.nav span:last-child{border-right:none}

/* hero */
.hero{left:133px;top:128px;width:902px;height:375px;
  background:linear-gradient(180deg,#5f8fb0 0%,#4f7a5a 55%,#6e9a3c 100%)}
.hero-box{left:190px;top:238px;width:327px;height:149px;background:rgba(26,160,224,.95);color:var(--white);
  padding:26px 0 0 28px;font-family:"Raleway",sans-serif}
.hero-box h1{font-size:29px;font-weight:500;line-height:1.1;white-space:nowrap}
.hero-box h2{font-size:15.5px;font-weight:400;margin-top:3px;white-space:nowrap}
.hero-box p{font-family:"Open Sans",sans-serif;font-size:10.5px;line-height:15px;margin-top:10px;white-space:nowrap}
.dots{left:557px;top:483px;display:flex;gap:4px}
.dots i{width:10px;height:10px;border-radius:50%;background:var(--white)}

/* services */
.services{left:133px;top:503px;width:902px;height:226px;display:flex;box-shadow:0 6px 10px rgba(0,0,0,.12)}
.service{flex:1;background:linear-gradient(180deg,#fff 0%,#f4f4f4 100%);border-right:1px solid var(--line);
  text-align:center;font-family:"Raleway",sans-serif;position:relative}
.service:last-child{border-right:none}
.service-icon{position:absolute;left:52px;top:34px;width:76px;height:76px;border-radius:50%}
.service h3{position:absolute;left:0;right:0;font-size:16px;font-weight:500;line-height:19px}
.service p{position:absolute;left:12px;right:12px;font-family:"Open Sans",sans-serif;font-size:10px;line-height:17px;color:#7a7a7a}
.service .more{position:absolute;left:0;right:0;font-size:11.5px;font-weight:600;color:#444}

/* content */
.content{left:133px;top:729px;width:902px;height:368px;background:var(--white)}
.col-title{font-family:"Raleway",sans-serif;font-size:20px;font-weight:400;white-space:nowrap}
.body-text{font-size:9.9px;line-height:17px;color:#555}
.lead{font-size:12px;color:#444;font-family:"Raleway",sans-serif}
.btn{width:101px;height:30px;border-radius:3px;color:var(--white);font-family:"Raleway",sans-serif;
  font-size:11px;font-weight:600;display:flex;align-items:center;justify-content:center;box-shadow:0 2px 3px rgba(0,0,0,.25)}
.btn-blue{background:linear-gradient(180deg,#1c6fcf,var(--navy))}
.btn-red{background:linear-gradient(180deg,var(--red),var(--red-dark))}

.about{left:156px;top:810px;width:282px}
.panel{left:453px;top:791px;width:294px;height:271px;background:linear-gradient(180deg,#f7f7f7,#e7e7e7);border:1px solid #e2e2e2}
.blog{left:767px;top:810px;width:260px}
.blog .body-text{font-size:9.6px;white-space:nowrap}

/* footer */
.footer{left:0;top:1097px;width:1168px;height:103px;background:var(--footer)}
.footer-links{left:136px;top:1123px;font-family:"Raleway",sans-serif;font-size:12px;color:#555}
.footer-links b{font-weight:400;margin:0 5px;color:#888}
.copy{left:136px;top:1148px;font-size:10.5px;color:#666}
.social{right:136px;top:1122px;display:flex;gap:8px}
.social i{width:20px;height:20px;border-radius:50%;background:#6f6f6f}
</style>
</head>
<body>

<div class="abs brand">
  <div class="brand-mark" role="img" aria-label="Brisk Tails emblem area"></div>
  <div class="brand-name">BRISK TAILS</div>
  <div class="brand-tag">HAPPY DOGS, HAPPY OWNERS</div>
</div>

<div class="abs call">
  <div class="call-label">Call Us Now</div>
  <div class="call-number">
    <svg width="15" height="15" viewBox="0 0 24 24" aria-hidden="true"><path fill="#fff" d="M6.6 10.8a15.2 15.2 0 0 0 6.6 6.6l2.2-2.2a1 1 0 0 1 1-.25 11.4 11.4 0 0 0 3.6.57 1 1 0 0 1 1 1V20a1 1 0 0 1-1 1A17 17 0 0 1 3 4a1 1 0 0 1 1-1h3.5a1 1 0 0 1 1 1c0 1.25.2 2.45.57 3.57a1 1 0 0 1-.25 1z"/></svg>
    555.204.7316
  </div>
</div>

<nav class="abs nav">
  <span>Home</span><span>About Us</span><span>Services</span><span>Dog Training</span><span>Testimonials</span><span>Dog Care</span><span>Contact</span>
</nav>

<div class="abs hero" role="img" aria-label="Photo of a woman training a brown dog beside a mountain lake"></div>
<div class="abs hero-box">
  <h1>Dog Training &amp; Care</h1>
  <h2>Vivamus porttitor purus nisi eleifend</h2>
  <p>Ut nisi erat fermentum vel congue id euismod in elit<br>Fusce ultricies orci ac feugiat suscipit leo mass</p>
</div>
<div class="abs dots"><i></i><i></i><i></i><i></i></div>

<section class="abs services">
  <div class="service">
    <div class="service-icon" role="img" aria-label="Dog training icon" style="background:var(--red)"></div>
    <h3 style="top:128px;color:var(--red)">Dog Training</h3>
    <p style="top:148px">Aetur ridiculus mus In iaculis facilisis massa Etiam ur</p>
    <div class="more" style="top:190px">READ MORE</div>
  </div>
  <div class="service">
    <div class="service-icon" role="img" aria-label="Nutrition profiling icon" style="background:var(--amber)"></div>
    <h3 style="top:131px;color:var(--amber-text)">Nutrition Profiling</h3>
    <p style="top:151px">Aetur ridiculus mus In iaculis facilisis massa Eti</p>
    <div class="more" style="top:193px">READ MORE</div>
  </div>
  <div class="service">
    <div class="service-icon" role="img" aria-label="Behavioural modification icon" style="background:var(--navy)"></div>
    <h3 style="top:117px;color:var(--blue-text)">Behavioural<br>Modification</h3>
    <p style="top:156px">Aetur ridiculus mus In iaculis facilisis massa Etiam ur</p>
    <div class="more" style="top:198px">READ MORE</div>
  </div>
  <div class="service">
    <div class="service-icon" role="img" aria-label="Puppy minding icon" style="background:var(--green)"></div>
    <h3 style="top:130px;color:var(--green-text)">Puppy Minding</h3>
    <p style="top:150px">Aetur ridiculus mus In iaculis facilisis massa Etiam urna</p>
    <div class="more" style="top:192px">READ MORE</div>
  </div>
  <div class="service">
    <div class="service-icon" role="img" aria-label="Health care icon" style="background:var(--grey-icon)"></div>
    <h3 style="top:127px;color:#555">Health Care</h3>
    <p style="top:147px">Aetur ridiculus mus In iaculis facilisis massa Etiam urna</p>
    <div class="more" style="top:189px">READ MORE</div>
  </div>
</section>

<main class="abs content"></main>

<section class="abs about">
  <h2 class="col-title" style="color:#333">ABOUT BRISK TAILS</h2>
  <p class="lead" style="margin-top:8px">Lorem ipsum dolor sit amet consectetuer</p>
  <p class="body-text" style="margin-top:5px">nascetur ridiculus mus In iaculis facilisis massa Etiam eu urna Sed porta Suspendisse quam leo molestie sed luctus quis feugiat in pede Fusce tellus Sed metus augue convallis et vehicula ut pulvinar eu ante Integer orci tellus</p>
  <p class="body-text" style="margin-top:5px">Class aptent taciti sociosqu ad litora torquent per conubia nostra per inceptos hymenaeos Proin nulla arcu Class aptent taciti sociosqu ad litora torquent per</p>
</section>
<div class="abs btn btn-blue" style="left:154px;top:1005px">READ MORE</div>

<section class="abs panel">
  <h2 class="col-title abs" style="left:18px;top:26px;color:var(--red)">How We Training</h2>
  <div class="abs" role="img" aria-label="Photo of a woman giving a hand signal to a golden retriever" style="left:18px;top:51px;width:258px;height:98px;background:linear-gradient(135deg,#6f9ee0,#86acd8 60%,#a9b77a)"></div>
  <p class="body-text abs" style="left:18px;top:158px;width:262px">Aliquet felis at cursus magna nisl nec elit Praesent elementum elit at tellus nec ultricies sit amet porttitor mattis enim In massa libero interdum nec</p>
</section>
<div class="abs btn btn-red" style="left:469px;top:1005px">READ MORE</div>

<section class="abs blog">
  <h2 class="col-title" style="color:var(--blue-text)">Latest Blog Post</h2>
  <p class="lead" style="margin-top:9px">Aascetur ridiculus mus iaculis</p>
  <p class="body-text" style="margin-top:3px">molestie sed luctus quis feugiat in pede Fusce tellus<br>etus augue aliquet felis at cursus</p>
  <p class="lead" style="margin-top:10px">Class aptent taciti socios</p>
  <p class="body-text" style="margin-top:3px">molestie sed luctus quis feugiat in pede Fusce tellus</p>
  <p class="lead" style="margin-top:10px">Fusce ultricies orci</p>
  <p class="body-text" style="margin-top:1px">Fusce tellus Sed metus augue aliquet felis at cursus</p>
</section>
<div class="abs btn btn-red" style="left:767px;top:1005px">READ MORE</div>

<footer class="abs footer"></footer>
<div class="abs footer-links">Home<b>|</b>About Us<b>|</b>Services<b>|</b>Dog Training<b>|</b>Testimonials<b>|</b>Dog Care<b>|</b>Contact</div>
<div class="abs copy">© 2014 Company Name &nbsp;All right reserved &nbsp;Term of Use</div>
<div class="abs social" aria-label="Social links"><i></i><i></i><i></i></div>

</body>
</html>
```